Tufted Hollow is company name.Handknit&crochet blankets&scarves. Need logo&business ...

I need a design that is eye catching, using yarn and is flowing. I'd like to see colors in aqua (Larkin Peabody paint LP9043 Aquastone) for the yarn and company name. For the text, a dark grey color (Larkin Peabody LP7622 Hamburg Gray)

Colors
87cfc7

```html
<!DOCTYPE html>
<html lang="en">
<head>
<meta charset="utf-8">
<title>Tufted Hollow — Business Card</title>
<link rel="stylesheet" href="https://fonts.googleapis.com/css2?family=Crimson+Text:ital,wght@0,400;1,400&family=Alegreya+Sans:ital,wght@1,500&display=swap">
<style>
  :root {
    --backdrop: #2b2c2e;
    --card-white: #ffffff;
    --card-blue: #8fadbd;
    --accent: #8fb1c3;
    --text-grey: #5b5f63;
    --on-blue: #ffffff;
  }
  * { margin: 0; padding: 0; box-sizing: border-box; }
  html, body { width: 1200px; height: 900px; overflow: hidden; }
  body {
    background: var(--backdrop);
    display: flex;
    flex-direction: column;
    align-items: center;
    justify-content: center;
    gap: 48px;
    font-family: "Crimson Text", Georgia, serif;
  }
  .card {
    position: relative;
    width: 640px;
    height: 366px;
    box-shadow: 0 10px 30px rgba(0,0,0,.45);
  }

  /* Front */
  .card--front { background: var(--card-white); color: var(--text-grey); }
  .holder-name {
    position: absolute; left: 44px; top: 40px;
    font-family: "Alegreya Sans", Arial, sans-serif;
    font-style: italic; font-weight: 500;
    font-size: 30px; letter-spacing: .5px;
  }
  .contact {
    position: absolute; left: 44px; top: 170px;
    list-style: none; font-size: 19px; font-style: italic; line-height: 1.35;
  }
  .contact li { display: flex; align-items: center; gap: 8px; }
  .contact svg { width: 14px; height: 14px; fill: var(--accent); flex: none; }
  .divider {
    position: absolute; left: 40px; right: 40px; top: 238px;
    height: 1px; background: var(--accent);
  }
  .brand {
    position: absolute; display: flex; align-items: center; gap: 12px;
    font-family: "Crimson Text", Georgia, serif; font-weight: 400;
  }
  .card--front .brand { right: 44px; top: 150px; font-size: 38px; color: var(--accent); }
  .brand-dot { border-radius: 50%; background: currentColor; flex: none; }
  .card--front .brand-dot { width: 30px; height: 30px; }

  .services {
    position: absolute; right: 44px; top: 252px;
    list-style: none; text-align: right; font-size: 19px; line-height: 1.3;
  }
  .services li { display: flex; justify-content: flex-end; align-items: center; gap: 10px; }
  .bullet { width: 9px; height: 9px; border-radius: 50%; background: var(--accent); }

  /* Back */
  .card--back { background: var(--card-blue); color: var(--on-blue); }
  .card--back .brand { left: 50%; top: 110px; transform: translateX(-50%); font-size: 58px; white-space: nowrap; }
  .card--back .brand-dot { width: 44px; height: 44px; }
  .service-line {
    position: absolute; left: 0; right: 0; bottom: 48px;
    display: flex; justify-content: center; align-items: center; gap: 12px;
    list-style: none; font-size: 19px; letter-spacing: .3px;
  }
  .service-line .bullet { background: var(--on-blue); }
</style>
</head>
<body>

  <section class="card card--front" aria-label="Business card front">
    <h1 class="holder-name">Maren Holloway</h1>

    <ul class="contact">
      <li>
        <svg viewBox="0 0 24 24" aria-hidden="true"><path d="M6.6 10.8a15.1 15.1 0 0 0 6.6 6.6l2.2-2.2a1 1 0 0 1 1-.25 11.4 11.4 0 0 0 3.6.57 1 1 0 0 1 1 1V20a1 1 0 0 1-1 1A17 17 0 0 1 3 4a1 1 0 0 1 1-1h3.5a1 1 0 0 1 1 1c0 1.25.2 2.45.57 3.57a1 1 0 0 1-.25 1z"/></svg>
        0555-0142-318
      </li>
      <li>
        <svg viewBox="0 0 24 24" aria-hidden="true"><path d="M2 5h20v14H2zm2 2v.5l8 5 8-5V7l-8 5z"/></svg>
        info@tuftedhollow.com
      </li>
    </ul>

    <div class="brand"><span class="brand-dot"></span>Tufted Hollow</div>

    <div class="divider"></div>

    <ul class="services">
      <li>Hand Knit Crochet <span class="bullet"></span></li>
      <li>Baby Afghans <span class="bullet"></span></li>
      <li>Afghans <span class="bullet"></span></li>
      <li>Scarves, Gloves, Hats <span class="bullet"></span></li>
    </ul>
  </section>

  <section class="card card--back" aria-label="Business card back">
    <div class="brand"><span class="brand-dot"></span>Tufted Hollow</div>
    <ul class="service-line">
      <li>Hand Knit Crochet</li><li class="bullet"></li>
      <li>Baby Afghans</li><li class="bullet"></li>
      <li>Afghans</li><li class="bullet"></li>
      <li>Scarves, Gloves, Hats</li>
    </ul>
  </section>

</body>
</html>
```